Quillory Nest Business Card

I need a business card design. We are a collaborate online training company. Our colors are gray and green. Our website is QuilloryNest.com

I would like an area for a profile picture within the card

```html
<!DOCTYPE html>
<html lang="en">
<head>
<meta charset="utf-8">
<title>Quillory Nest Business Card</title>
<link href="https://fonts.googleapis.com/css2?family=Roboto+Slab:wght@300;400;700&display=swap" rel="stylesheet">
<style>
  :root{
    --bg:#e9e7e3;
    --card:#231f20;
    --green:#7cc242;
    --green-dark:#5a9a2c;
    --blue:#2aa7df;
    --white:#ffffff;
    --muted:#b9b9b9;
  }
  *{box-sizing:border-box;margin:0;padding:0}
  html,body{width:1200px;height:913px;overflow:hidden;background:var(--bg)}
  body{position:relative;font-family:"Roboto Slab",serif}
  .card{position:absolute;width:525px;height:300px;background:var(--card);overflow:hidden;box-shadow:0 6px 18px rgba(0,0,0,.18)}
  .card--front{left:337px;top:100px}
  .card--back{left:337px;top:470px}

  /* front */
  .brand{position:absolute;left:0;right:0;top:80px;display:flex;align-items:center;justify-content:center;gap:14px}
  .brand__dot{width:30px;height:30px;border-radius:50%;background:var(--green)}
  .brand__name{font-weight:700;font-size:42px;color:var(--white);letter-spacing:-.5px;white-space:nowrap}
  .front-band{position:absolute;left:0;top:188px;width:525px;height:44px}
  .front-band__url{position:absolute;left:0;right:0;top:197px;text-align:center;color:var(--white);font-size:18px;font-weight:400}

  /* back */
  .accent-art{position:absolute;right:0;top:0;width:250px;height:100px;background:linear-gradient(200deg,var(--green) 0%,var(--green-dark) 55%,var(--card) 100%)}
  .portrait{position:absolute;left:52px;top:62px;width:130px;height:104px}
  .portrait__tile{position:absolute;inset:0}
  .portrait__tile--blue{background:var(--blue);transform:rotate(-8deg)}
  .portrait__tile--green{background:var(--green);transform:rotate(6deg)}
  .portrait__photo{position:absolute;inset:0;border:4px solid var(--white);background:linear-gradient(160deg,#e4e4e4,#a9a9a9)}
  .person{position:absolute;left:52px;top:186px}
  .person__name{font-size:20px;line-height:24px;color:var(--white);font-weight:400;white-space:nowrap}
  .person__surname{color:var(--green);font-weight:700}
  .person__role{font-size:10px;line-height:13px;color:var(--muted)}
  .contact{position:absolute;left:52px;top:234px;list-style:none;font-size:9.5px;color:var(--white);line-height:14px}
  .contact li{display:flex;align-items:center;gap:6px;white-space:nowrap}
  .contact__icon{width:10px;height:10px;flex:none}
  .divider{position:absolute;left:300px;top:190px;width:1px;height:78px;background:var(--green)}
  .office{position:absolute;left:318px;top:200px;font-size:10px;line-height:14px;color:var(--white);white-space:nowrap}
  .office__title{color:var(--green);font-weight:700}
</style>
</head>
<body>

<section class="card card--front" aria-label="Card front">
  <div class="brand">
    <span class="brand__dot"></span>
    <span class="brand__name">Quillory Nest</span>
  </div>
  <svg class="front-band" viewBox="0 0 525 44" aria-hidden="true">
    <line x1="0" y1="40" x2="60" y2="40" stroke="#7cc242" stroke-width="2"/>
    <line x1="465" y1="4" x2="525" y2="4" stroke="#7cc242" stroke-width="2"/>
    <polygon points="60,30 80,4 465,4 465,14 445,40 60,40" fill="#7cc242"/>
  </svg>
  <div class="front-band__url">www.quillorynest.com</div>
</section>

<section class="card card--back" aria-label="Card back">
  <div class="accent-art" role="img" aria-label="Green decorative accent area"></div>

  <div class="portrait">
    <div class="portrait__tile portrait__tile--blue"></div>
    <div class="portrait__tile portrait__tile--green"></div>
    <div class="portrait__photo" role="img" aria-label="Profile photo of the founder"></div>
  </div>

  <div class="person">
    <div class="person__name">Dorian <span class="person__surname">HALVIK</span></div>
    <div class="person__role">Founder</div>
  </div>

  <ul class="contact">
    <li><svg class="contact__icon" viewBox="0 0 10 10" aria-hidden="true"><circle cx="5" cy="5" r="5" fill="#7cc242"/><rect x="2.3" y="3" width="5.4" height="4" fill="none" stroke="#231f20" stroke-width=".8"/><path d="M2.3 3 L5 5.2 L7.7 3" fill="none" stroke="#231f20" stroke-width=".8"/></svg>info@quillorynest.com</li>
    <li><svg class="contact__icon" viewBox="0 0 10 10" aria-hidden="true"><circle cx="5" cy="5" r="5" fill="#7cc242"/><path d="M3.3 2.6 L4.3 3.8 L3.8 4.6 C4.3 5.5 4.7 5.9 5.5 6.3 L6.3 5.8 L7.4 6.8 L6.8 7.5 C5 7.3 2.8 5.2 2.6 3.3 Z" fill="#231f20"/></svg>(555) 014-2297</li>
    <li><svg class="contact__icon" viewBox="0 0 10 10" aria-hidden="true"><circle cx="5" cy="5" r="5" fill="#7cc242"/><circle cx="5" cy="5" r="2.6" fill="none" stroke="#231f20" stroke-width=".8"/><line x1="2.4" y1="5" x2="7.6" y2="5" stroke="#231f20" stroke-width=".7"/><ellipse cx="5" cy="5" rx="1.1" ry="2.6" fill="none" stroke="#231f20" stroke-width=".7"/></svg>www.quillorynest.com</li>
  </ul>

  <div class="divider"></div>

  <div class="office">
    <div class="office__title">Administrative Office</div>
    <div>482 Marlow Crest Ave. Suite 7</div>
    <div>Fenwick, Oregon 97021</div>
    <div>(555) 014-2297</div>
  </div>
</section>

</body>
</html>
```